Delivery Docket urgent plus require many other designs for more stationary after this.

We need a new delivery docket design urgently as the one we have needs updating and we have changed our company name. Please do not copy the one I have uploaded as we do not feel this looks professional enough. I uploaded it as a few designers requested to see what we are currently using thank you.
It is quite complex in that we need a range of information to be on the one docket.
We are a Transport Company based in Australia that has a wide variety of items that we deliver such as water, sand and gravels and heavy equipment transport.
We would prefer to keep this design to A5 size as we will get them made into books. We are looking for a modern professional look. Although it is only a delivery docket this is given to all our customers so needs to look impressive.

We need our new logo on the docket (PRW). There will also need to be areas for our address and contact numbers, email etc these will be supplied to the winning designer to make the final adjustments so for now just put something generic in these spaces.
Needs to have an area for customer details, purchase order number, date and docket number (docket number to be in red)
Needs a section where we can list the type of product / and or service that has been provided and the amount / qty usually 3 lines will be enough for this. Need area under this where the customer can sign name and print name to say that the goods / and or services have been received.

Also required somewhere on the docket are the words, Tax Invoice will be issued based on the information provided on this docket. Conditions on back of page

We then need a separate section on the same page which we will use internally that the staff member can tear off and hand into the office. On this section it needs to have area where the driver can list km at start of job and at end with space to calculate km travelled, details of fuel purchased eg amount and litres, vehicle that is being used. also need to log down wheel bearing temps.
prime mover needs spaces as follows
Steer axel FL____________ Steer axel FR _________ 1st drive axel L_______
1st drive axel R_________ 2nd drive axel L_______ 2nd drive axel R________

For the trailers need something similar x 2 as have 2 trailers
1st axel DS_________ 1st axel PS_________ 2nd axel DS__________
2nd axel PS_________ 3rd axel DS_________ 3rd axel PS__________

I have included a few examples of designs we have used in past and ones that we like so you can get an idea of the colours we prefer, I have included some of the designs we are currently receiving for our logo that I like so you can get idea again of colours we prefer. There is much more we need designed also such as time sheets, more delivery dockets and letter heads so there is a lot of more work available to the winning designer.

Thank you

Target Market(s)

Customers

Font styles to use
Serif
Sans Serif

Colors

Designer to choose colors to be used in the design.

Requirements
Should not have
• Please don't copy old docket as we do not like it and nned new info on new design thank you

```html
<!DOCTYPE html>
<html lang="en">
<head>
<meta charset="utf-8">
<title>PRW Delivery Docket</title>
<link rel="stylesheet" href="https://fonts.googleapis.com/css2?family=Open+Sans:ital,wght@0,400;0,600;0,700;1,600;1,700&display=swap">
<style>
:root{
  --ink:#111;
  --dark:#0c0c0c;
  --panel:#d8d8d8;
  --row:#d3d3d3;
  --row-alt:#e0e0e0;
  --field:#ffffff;
  --accent:#29b8d8;
  --docket-red:#c4161c;
  --white:#ffffff;
  --brand:#cfcfcf;
}
*{box-sizing:border-box;margin:0;padding:0}
html,body{width:1200px;height:847px;overflow:hidden;background:var(--dark)}
body{font-family:"Open Sans",Arial,sans-serif;color:var(--ink)}
.docket{position:relative;width:1190px;height:840px;transform:scale(1.0084);transform-origin:0 0;overflow:hidden;background:var(--dark)}
.abs{position:absolute}
.backdrop{position:absolute;inset:0;background:radial-gradient(ellipse at 50% 45%,#4a4a4a 0%,#262626 35%,#101010 75%)}
.top-rule{left:0;right:0;top:28px;height:4px;background:var(--accent)}
.header-rule{top:130px;height:3px;background:var(--accent)}
.brand{left:52px;top:42px;width:216px;text-align:center;font-weight:700;font-size:62px;letter-spacing:10px;color:var(--brand);line-height:1}
.head-label{font-size:21px;color:var(--white);line-height:1}
.head-field{background:var(--field);height:33px}
.head-line{height:2px;background:var(--accent)}
.docket-no{color:var(--docket-red);font-weight:700;font-size:21px;text-align:right;padding:4px 8px 0 0}
.date-field{font-size:20px;color:#333;padding-top:3px}
.tag{font-style:italic;font-weight:700;font-size:17px;color:var(--accent);letter-spacing:.5px}
.party{background:var(--panel);top:133px;height:159px}
.supplier{left:0;width:567px;padding:15px 28px;font-size:21px;line-height:32px}
.supplier b{font-weight:700;margin-right:36px}
.customer{left:623px;width:567px;padding:18px 28px 0 23px}
.customer-line{display:flex;align-items:flex-end;height:32px;border-bottom:1px solid #b5b5b5;font-size:16px;font-weight:600;color:#222;padding-bottom:4px}
.col-head{color:var(--white);font-size:21px;font-weight:600;top:318px}
.items{left:28px;top:351px;width:1134px;border:1px solid #aaa}
.item-row{display:flex;height:40px;background:var(--row);border-bottom:1px solid #aaa}
.item-row:nth-child(2){background:var(--row-alt)}
.item-row:last-child{border-bottom:0}
.item-qty{width:120px;border-right:2px solid #aaa}
.notice{left:38px;top:493px;color:var(--white);font-style:italic;font-weight:600;font-size:16.5px;line-height:22px}
.sign-box{top:492px;height:67px;background:var(--panel);font-size:16px;font-weight:400;padding:4px 7px}
.office{left:0;right:0;top:572px;bottom:0;background:linear-gradient(180deg,#dedede,#d4d4d4)}
.group-title{font-size:19px;text-align:center;border-bottom:2px solid var(--accent);height:38px;padding-top:8px}
.field-label{font-size:17px;line-height:34px}
.box{background:var(--field);height:34px}
.bearing-row{display:flex;align-items:center;height:30px;margin-bottom:8px}
.bearing-row .lbl{font-size:17px;text-align:right;padding-right:6px;white-space:nowrap}
.bearing-row .box{height:30px}
sup{font-size:10px}
</style>
</head>
<body>
<main class="docket">
  <div class="backdrop" role="img" aria-label="Dark metal mesh background texture"></div>
  <div class="abs top-rule"></div>

  <header>
    <div class="abs brand">PRW</div>
    <span class="abs head-label" style="left:313px;top:64px">Docket N</span>
    <div class="abs head-field docket-no" style="left:430px;top:57px;width:137px">2050</div>
    <div class="abs head-line" style="left:313px;top:90px;width:254px"></div>

    <span class="abs head-label" style="left:624px;top:64px">Order N</span>
    <div class="abs head-field" style="left:740px;top:57px;width:136px"></div>
    <div class="abs head-line" style="left:624px;top:90px;width:252px"></div>

    <span class="abs head-label" style="left:908px;top:64px">Date</span>
    <div class="abs head-field date-field" style="left:975px;top:57px;width:187px"><span style="margin-left:60px">/</span><span style="margin-left:52px">/</span></div>
    <div class="abs head-line" style="left:908px;top:90px;width:254px"></div>

    <span class="abs tag" style="left:476px;top:113px">SUPPLIER</span>
    <span class="abs tag" style="left:624px;top:113px">CUSTOMER</span>
  </header>
  <div class="abs header-rule" style="left:0;width:567px"></div>
  <div class="abs header-rule" style="left:623px;right:0"></div>

  <section class="abs party supplier">
    <div><b>PRW</b>ABN 00 000 000 000</div>
    <div>Street Address,&nbsp; Town</div>
    <div>000 000 000</div>
    <div>your_email@yourdomain.com</div>
  </section>
  <section class="abs party customer">
    <div class="customer-line">NAME:</div>
    <div class="customer-line">CONTACT:</div>
    <div class="customer-line">PHONE:</div>
    <div class="customer-line">BILLING ADDRESS:</div>
  </section>

  <span class="abs col-head" style="left:70px">Qty</span>
  <span class="abs col-head" style="left:529px">Description</span>
  <div class="abs items">
    <div class="item-row"><div class="item-qty"></div></div>
    <div class="item-row"><div class="item-qty"></div></div>
    <div class="item-row"><div class="item-qty"></div></div>
  </div>

  <p class="abs notice">Tax Invoice will be issued based on<br>the information provided on this docket.<br>Conditions on back of page</p>
  <div class="abs sign-box" style="left:385px;width:345px">GOODS RECEIVED BY</div>
  <div class="abs sign-box" style="left:740px;width:409px">SIGNED</div>

  <section class="abs office">
    <div class="abs group-title" style="left:28px;top:1px;width:362px">Distance</div>
    <span class="abs field-label" style="left:28px;top:44px">Start</span>
    <div class="abs box" style="left:74px;top:44px;width:74px"></div>
    <span class="abs field-label" style="left:160px;top:44px">End</span>
    <div class="abs box" style="left:197px;top:44px;width:73px"></div>
    <span class="abs field-label" style="left:286px;top:44px">Km</span>
    <div class="abs box" style="left:318px;top:44px;width:72px"></div>

    <div class="abs group-title" style="left:414px;top:1px;width:363px">Fuel</div>
    <span class="abs field-label" style="left:414px;top:44px">Amount</span>
    <div class="abs box" style="left:489px;top:44px;width:107px"></div>
    <span class="abs field-label" style="left:615px;top:44px">Litres</span>
    <div class="abs box" style="left:669px;top:44px;width:108px"></div>

    <div class="abs group-title" style="left:799px;top:1px;width:363px">Vehicle</div>
    <div class="abs box" style="left:799px;top:44px;width:363px"></div>

    <div class="abs group-title" style="left:28px;top:82px;width:362px">Prime mover</div>
    <div class="abs" style="left:20px;top:130px">
      <div class="bearing-row"><span class="lbl" style="width:123px">Steer axel FL</span><div class="box" style="width:62px"></div><span class="lbl" style="width:124px">Steer axel FR</span><div class="box" style="width:62px"></div></div>
      <div class="bearing-row"><span class="lbl" style="width:123px">1<sup>st</sup> dr. axel L</span><div class="box" style="width:62px"></div><span class="lbl" style="width:124px">1<sup>st</sup> dr. axel R</span><div class="box" style="width:62px"></div></div>
      <div class="bearing-row"><span class="lbl" style="width:123px">2<sup>nd</sup> dr. axel L</span><div class="box" style="width:62px"></div><span class="lbl" style="width:124px">2<sup>nd</sup> dr. axel R</span><div class="box" style="width:62px"></div></div>
    </div>

    <div class="abs group-title" style="left:414px;top:82px;width:363px">Trailer 1</div>
    <div class="abs" style="left:404px;top:130px">
      <div class="bearing-row"><span class="lbl" style="width:112px">1<sup>st</sup> axel DS</span><div class="box" style="width:68px"></div><span class="lbl" style="width:125px">1<sup>st</sup> axel PS</span><div class="box" style="width:68px"></div></div>
      <div class="bearing-row"><span class="lbl" style="width:112px">2<sup>nd</sup> axel DS</span><div class="box" style="width:68px"></div><span class="lbl" style="width:125px">2<sup>nd</sup> axel PS</span><div class="box" style="width:68px"></div></div>
      <div class="bearing-row"><span class="lbl" style="width:112px">3<sup>rd</sup> axel DS</span><div class="box" style="width:68px"></div><span class="lbl" style="width:125px">3<sup>rd</sup> axel PS</span><div class="box" style="width:68px"></div></div>
    </div>

    <div class="abs group-title" style="left:799px;top:82px;width:363px">Trailer 2</div>
    <div class="abs" style="left:790px;top:130px">
      <div class="bearing-row"><span class="lbl" style="width:114px">1<sup>st</sup> axel DS</span><div class="box" style="width:68px"></div><span class="lbl" style="width:122px">1<sup>st</sup> axel PS</span><div class="box" style="width:68px"></div></div>
      <div class="bearing-row"><span class="lbl" style="width:114px">2<sup>nd</sup> axel DS</span><div class="box" style="width:68px"></div><span class="lbl" style="width:122px">2<sup>nd</sup> axel PS</span><div class="box" style="width:68px"></div></div>
      <div class="bearing-row"><span class="lbl" style="width:114px">3<sup>rd</sup> axel DS</span><div class="box" style="width:68px"></div><span class="lbl" style="width:122px">3<sup>rd</sup> axel PS</span><div class="box" style="width:68px"></div></div>
    </div>
  </section>
</main>
</body>
</html>
```